Brill Insurance Agency - Business Cards

Hello, I am needing new trendy business cards for our Insurance Agency now that I have a new Logo. I have attached our new logo with several color options along with a business card design that I like. I am leaning towards burgundy and blue colors. I have attached our current business card. I have also attached a headshot of our company president, Martin Vale, that you can use if you wish. Thank you so much in advance for all the wonderful designs!!!!

Target Market(s)

We want to look very professional to potential customers and we also want to look very professional so insurance companies will want to contract with us to sell their product.

Industry/Entity Type

Insurance

Contact Information for Business Card

Martin Vale
mvale@brillagency.com
Business: 555-213-4087
Fax: 555-213-7751
Cell: 555-390-2618
Toll Free: 888-555-0194
42 W Elm Rd Butler, MO 64730
www.brillagency.net

Font styles to use
Serif
Sans Serif

Colors
0355a3
3277b5
f04a50
ec1f27

Requirements
Nice to have
• I love creativity. The more creative and balanced a business card design the more I will like it. I would like the card to be printed horizontally instead of vertically.
Should not have
• My project should not have the Allied Coverage Network logo. It is no longer used in the industry.

```html
<!DOCTYPE html>
<html lang="en">
<head>
<meta charset="utf-8">
<title>Brill Insurance Agency – Business Cards</title>
<link rel="stylesheet" href="https://fonts.googleapis.com/css2?family=Montserrat:wght@500;600;700&display=swap">
<style>
  :root {
    --teal: #16a98f;
    --charcoal: #4a4a4a;
    --ink: #3d3d3d;
    --white: #ffffff;
    --frame: #2b2b2b;
    --photo-top: #8a8a86;
    --photo-bottom: #2c2f35;
  }
  * { margin: 0; padding: 0; box-sizing: border-box; }
  html, body { width: 1200px; height: 1000px; overflow: hidden; background: var(--white); }
  body { position: relative; font-family: "Montserrat", Arial, sans-serif; }

  .card {
    position: absolute; left: 314px; width: 580px; height: 340px;
    border: 1px solid var(--frame); overflow: hidden;
  }
  .card--front { top: 123px; background: var(--white); }
  .card--back  { top: 531px; background: var(--charcoal); }

  .card__shapes { position: absolute; inset: 0; }

  /* Agency name block */
  .brand { position: absolute; left: 38px; top: 18px; width: 510px; height: 90px; }
  .brand__dot {
    position: absolute; left: 2px; top: 6px; width: 78px; height: 78px;
    border-radius: 50%; background: var(--teal);
  }
  .brand__name {
    position: absolute; left: 114px; top: 0; width: 386px;
    color: var(--teal); font-weight: 700; white-space: nowrap;
  }
  .brand__line1 { display: block; font-size: 39.5px; line-height: 48px; letter-spacing: 0; }
  .brand__line2 {
    display: flex; align-items: center; gap: 10px;
    font-size: 24px; letter-spacing: 6px; line-height: 30px;
  }
  .brand__rule { flex: 1; height: 3px; background: var(--teal); }

  /* Contact list */
  .contact { position: absolute; list-style: none; }
  .contact__item {
    position: absolute; display: flex; align-items: center; gap: 9px;
    font-size: 14.5px; font-weight: 500; color: var(--ink); white-space: nowrap;
  }
  .contact__item--web { color: var(--white); }
  .contact__icon { width: 20px; height: 20px; flex: none; }

  /* Portrait */
  .portrait {
    position: absolute; left: 424px; top: 111px; width: 115px; height: 151px;
    border: 4px solid var(--charcoal);
    background: linear-gradient(180deg, var(--photo-top), var(--photo-bottom));
  }
  .person-name {
    position: absolute; left: 412px; top: 270px; width: 140px; text-align: center;
    color: var(--white); font-size: 19px; font-weight: 500; white-space: nowrap;
  }

  /* Address strip */
  .address {
    position: absolute; left: 84px; top: 307px; display: flex; align-items: center; gap: 16px;
    color: var(--white); font-size: 16.5px; font-weight: 500; white-space: nowrap;
  }
  .address__icon { width: 18px; height: 24px; }

  /* Back */
  .back-brand {
    position: absolute; left: 0; right: 0; top: 145px;
    display: flex; align-items: center; justify-content: center; gap: 12px;
    color: var(--white); font-weight: 700; font-size: 20px; letter-spacing: 1px;
  }
  .back-brand__dot { width: 40px; height: 40px; border-radius: 50%; background: var(--white); }
</style>
</head>
<body>

<section class="card card--front" aria-label="Business card front">
  <svg class="card__shapes" viewBox="0 0 580 340" width="580" height="340" aria-hidden="true">
    <polygon points="231,130 580,130 580,300 58,300" fill="var(--teal)"/>
    <polygon points="189,130 218,130 44,300 13,300" fill="var(--charcoal)"/>
    <rect x="0" y="299" width="580" height="41" fill="var(--charcoal)"/>
  </svg>

  <div class="brand">
    <span class="brand__dot"></span>
    <h1 class="brand__name">
      <span class="brand__line1">BRILL INSURANCE</span>
      <span class="brand__line2"><span class="brand__rule"></span>AGENCY INC<span class="brand__rule"></span></span>
    </h1>
  </div>

  <ul class="contact">
    <li class="contact__item contact__item--web" style="left:237px;top:138px">
      <svg class="contact__icon" viewBox="0 0 20 20" fill="none" stroke="#fff" stroke-width="1.6"><circle cx="10" cy="10" r="8"/><ellipse cx="10" cy="10" rx="3.5" ry="8"/><line x1="2" y1="10" x2="18" y2="10"/><line x1="3.5" y1="6" x2="16.5" y2="6"/><line x1="3.5" y1="14" x2="16.5" y2="14"/></svg>
      www.brillagency.net
    </li>
    <li class="contact__item" style="left:209px;top:165px">
      <svg class="contact__icon" viewBox="0 0 20 20" fill="none" stroke="#fff" stroke-width="1.5"><rect x="1.5" y="4" width="17" height="12"/><polyline points="1.5,4 10,11 18.5,4"/></svg>
      mvale@brillagency.com
    </li>
    <li class="contact__item" style="left:183px;top:193px">
      <svg class="contact__icon" viewBox="0 0 20 20" fill="#fff"><polygon points="10,1 20,10 17,10 17,19 12,19 12,13 8,13 8,19 3,19 3,10 0,10"/></svg>
      555.390.2618
    </li>
    <li class="contact__item" style="left:155px;top:220px">
      <svg class="contact__icon" viewBox="0 0 20 20" fill="#fff"><rect x="5" y="1" width="10" height="5"/><rect x="1" y="7" width="18" height="8" rx="1"/><rect x="5" y="13" width="10" height="6"/></svg>
      555.213.7751
    </li>
    <li class="contact__item" style="left:130px;top:247px">
      <svg class="contact__icon" viewBox="0 0 20 20" fill="none" stroke="#fff" stroke-width="1.8"><rect x="5" y="1" width="10" height="18" rx="2"/><line x1="9" y1="15.5" x2="11" y2="15.5"/></svg>
      1-888.555.0194
    </li>
    <li class="contact__item" style="left:104px;top:272px">
      <svg class="contact__icon" viewBox="0 0 20 20" fill="#fff"><path d="M4 1 L8 5 L6 8 C7 11 9 13 12 14 L15 12 L19 16 L16 19 C8 18 2 12 1 4 Z"/></svg>
      555.213.4087 ext. 41
    </li>
  </ul>

  <div class="portrait" role="img" aria-label="Headshot of agency president Martin Vale"></div>
  <p class="person-name">Martin Vale</p>

  <p class="address">
    <svg class="address__icon" viewBox="0 0 18 24" fill="#fff"><path d="M9 0 C4 0 0 4 0 9 C0 15 9 24 9 24 C9 24 18 15 18 9 C18 4 14 0 9 0 Z M9 5 A4 4 0 1 1 9 13 A4 4 0 1 1 9 5 Z"/></svg>
    42 West Elm, P.O. Box 215, Ashford, Kansas 66990
  </p>
</section>

<section class="card card--back" aria-label="Business card back">
  <div class="back-brand">
    <span class="back-brand__dot"></span>
    <span>BRILL INSURANCE AGENCY INC</span>
  </div>
</section>

</body>
</html>
```